Law Firm in Texas in need of new letterhead

Law Firm in Fort Worth, TX, USA named "Pell & Whitcombe, Attorneys-At-Law, LLP." This is a general practice law firm that mostly does Family Law and Criminal Defense work.

We are looking for a new letterhead that has a "classical" appeal, with modern elements.

Any color combination is fine, but please note that we do fax many documents, so the design must be clearly legible in Black and White.

We would like our letterhead to project a sense of professionalism, integrity, and ability.

Target Market(s)

Letterhead will be for correspondence generally with other attorneys and clients.

Industry/Entity Type

Law Firm

Logo Text

Pell & Whitcombe, Attorneys-At-Law, LLP.

Logo styles of interest
Pictorial/Combination Logo
Wordmark Logo
Lettermark Logo
Requirements
Nice to have
• Although not necessary, a "Texas Star" that is incorporated into the design would be a nice touch.
Should not have
• Colors that do not convert to B&W easily

```html
<!DOCTYPE html>
<html lang="en">
<head>
<meta charset="utf-8">
<title>Pell &amp; Whitcombe Letterhead</title>
<link rel="stylesheet" href="https://fonts.googleapis.com/css2?family=Questrial&display=swap">
<style>
  :root {
    --backdrop: #c9cacc;
    --paper: #ffffff;
    --navy: #1f4a78;
    --ink: #4a4d52;
    --ink-dark: #2b2d30;
    --rule: #2f5d8c;
    --watermark-a: #eceef0;
    --watermark-b: #f7f8f9;
    --signature: #c9d1e6;
  }
  * { margin: 0; padding: 0; box-sizing: border-box; }
  html, body {
    width: 1200px; height: 1000px; overflow: hidden;
    background: var(--backdrop);
    font-family: "Questrial", "Century Gothic", sans-serif;
  }
  .letterhead {
    position: absolute; left: 237px; top: 30px;
    width: 726px; height: 940px;
    background: var(--paper);
    box-shadow: 0 2px 10px rgba(0,0,0,0.12);
  }
  .firm-name {
    position: absolute; left: 64px; top: 56px;
    display: flex; align-items: center; gap: 10px;
    color: var(--navy); font-size: 19px; letter-spacing: 0.5px;
  }
  .firm-name .mark-square {
    width: 14px; height: 14px; background: var(--navy);
  }
  .star-watermark {
    position: absolute; left: 233px; top: 300px;
    width: 260px; height: 260px; border-radius: 50%;
    background: radial-gradient(circle, var(--watermark-a) 0%, var(--watermark-b) 60%, var(--paper) 72%);
  }
  .letter-body {
    position: absolute; left: 300px; top: 190px; width: 362px;
    color: var(--ink); font-size: 10.5px; line-height: 1.55;
    text-align: justify;
  }
  .letter-body p { margin-bottom: 12px; }
  .sign-off {
    position: absolute; left: 300px; top: 580px; width: 362px;
    color: var(--ink); font-size: 10.5px;
  }
  .sign-off .closing { text-align: right; }
  .sign-off .signature-row {
    display: flex; justify-content: flex-end; align-items: center; gap: 14px; margin-top: 8px;
  }
  .sign-off .signature {
    width: 110px; height: 44px; border-radius: 6px;
    background: linear-gradient(90deg, var(--paper), var(--signature), var(--paper));
  }
  .sign-off .signatory { color: var(--ink-dark); font-size: 12px; font-weight: bold; }
  .letter-footer {
    position: absolute; left: 64px; right: 64px; top: 800px;
    text-align: center; font-size: 9.5px; color: var(--navy);
  }
  .letter-footer .rule { height: 1px; background: var(--rule); }
  .letter-footer .address { margin: 12px 0 6px; }
  .letter-footer .label { font-weight: bold; }
  .letter-footer .partner { margin-bottom: 5px; }
  .letter-footer .partner-name { font-weight: bold; text-transform: uppercase; }
  .letter-footer .credentials { color: var(--ink); }
</style>
</head>
<body>
  <main class="letterhead">
    <header class="firm-name">
      <span class="mark-square"></span>
      <span>Pell &amp; Whitcombe, Attorneys-At-Law, LLP.</span>
    </header>

    <div class="star-watermark" role="img" aria-label="Faint Texas star watermark"></div>

    <section class="letter-body">
      <p>Lorem ipsum dolor sit amet, consectetur adipiscing elit, sed do eiusmod tempor incididunt ut labore et dolore magna aliqua. Ut enim ad minim veniam, quis nostrud exercitation ullamco laboris nisi ut aliquip ex ea commodo consequat. Duis aute irure dolor in reprehenderit in voluptate velit esse cillum dolore eu fugiat nulla pariatur.</p>
      <p>Excepteur sint occaecat cupidatat non proident, sunt in culpa qui officia deserunt mollit anim id est laborum. Sed ut perspiciatis unde omnis iste natus error sit voluptatem accusantium doloremque laudantium.</p>
      <p>Excepteur sint occaecat cupidatat non proident, sunt in culpa qui officia deserunt mollit anim id est laborum. Sed ut perspiciatis unde omnis iste natus error sit voluptatem accusantium doloremque laudantium.</p>
      <p>Lorem ipsum dolor sit amet, consectetur adipiscing elit, sed do eiusmod tempor incididunt ut labore et dolore magna aliqua. Ut enim ad minim veniam, quis nostrud exercitation ullamco laboris nisi ut aliquip ex ea commodo consequat. Duis aute irure dolor in reprehenderit in voluptate velit esse cillum dolore eu fugiat nulla pariatur.</p>
    </section>

    <section class="sign-off">
      <p class="closing">Yours Sincerely,</p>
      <div class="signature-row">
        <div class="signature" role="img" aria-label="Handwritten signature"></div>
        <span class="signatory">Helen Marsh</span>
      </div>
    </section>

    <footer class="letter-footer">
      <div class="rule"></div>
      <p class="address">1840 W. Magnolia Ave., Fort Worth, TX 76110. <span class="label">Phone:</span> (817) 555-0142 &nbsp;<span class="label">Fax:</span> (817) 555-0187</p>
      <p class="partner"><span class="partner-name">Daniel Pell</span> - Managing Partner <span class="credentials">( Licensed in State of Texas, United States District Court (Northern District of Texas), United States Supreme Court )</span></p>
      <p class="partner"><span class="partner-name">Laura Anne Whitcombe</span> <span class="credentials">( Licensed in the State of Texas )</span></p>
    </footer>
  </main>
</body>
</html>
```